Coffee Bag Label

I need a coffee bag label designed (front label and back label):
Our company "Fenn-Brew" imports organic coffee beans direct from a farm on Vorsela Mountain on a private reserve (rainforest) from Jinotega, Nicaragua.
Labels should each be 3 inches x 3 inches (with room on edges for bleed). I want the front label to catch the eye and coordinate well with the coffee bag. The bags sizes are below and pictures are attached.
Bag sizes: Lime green 12 oz bag: 3-3/8" x 2-9/16" x 10-1/4"
Black 2 oz sample stand up pouch: 4" x 6-1/2" + 2-3/8", 2oz (60g)
Black 2lb bag: 5" x 3-3/8" x 15", 2lb (1kg)
Please include as much as possible below on the front label without it looking too wordy:
1) Our logo (it's attached). Feel free to do something creative with just the bean and place "Fenn-Brew" or "Tidy-Pod Coffees" somewhere else. They don't have to be together like in the attached file. The bean can be in the background of the label as well or something else cool like in the form of a cloud over the volcano or as the sun in the sky over the volcano.
2) lime green, burnt orange, dark brown & black
3) Front label should say:
"100% Premium Arabica Nicaraguan Coffee"
"Organic, Rain Forest & Mountain Shade Grown"
Bottom of label:
"Medium Roast"
"Full body, bold flavor, nutty, hints of chocolate, with a distinct & flavorful aroma."
I want one front label file for each size bag: "2 oz" "12 oz" & "32 oz"
Back of the label:
I have uploaded a hand drawn pic of what I am thinking but if you have a better idea please submit it.
Please include as much as possible below without it looking wordy:
Directions on the perfect cup:
***2 Tbsp high quality coffee 6 Oz. cup of pure filtered water
(these can be tied into the hand-drawn picture. I will label the section each one corresponds to)
Organically Grown (sustainable)
Rainforest Grown (sustainable)
Mountain Shade Grown (sustainable)
Hand Picked (select)
Spring Water Washed (select)
Sun Dried (select)
Social Responsibility (profits help fund Bright Path Outreach Nicaragua www.brightpathoutreach.example.org)
Single Source Coffee (Single source)
Traceable Source (single source)
Website: www.Tidy-Pod.example.com
Reason: I have been asked to extend deadline by a few designers.
Thanks,
Joanne Pelter
ages 18-54
- Should have a cool border. Maybe fade from one color to another or have something more original than just a 3x3 square border.

```html
<!DOCTYPE html>
<html lang="en">
<head>
<meta charset="utf-8">
<title>Fenn-Brew Front Label – 12 oz</title>
<link rel="stylesheet" href="https://fonts.googleapis.com/css2?family=Share+Tech+Mono&family=Space+Mono:wght@400;700&family=Lato:wght@400&display=swap">
<style>
  :root {
    --lime: #a9d04f;
    --lime-deep: #8bab3f;
    --brown: #6b4a2e;
    --bean-brown: #7a3622;
    --burnt-orange: #f26b3a;
    --ink: #1f1f1f;
    --panel-ink: #3b4722;
  }
  html, body {
    margin: 0;
    padding: 0;
    width: 1200px;
    height: 1200px;
    overflow: hidden;
  }
  .label {
    position: relative;
    width: 1200px;
    height: 1200px;
    background: var(--lime);
  }
  .brand-name {
    position: absolute;
    top: 160px;
    left: 0;
    width: 100%;
    margin: 0;
    text-align: center;
    font-family: "Share Tech Mono", monospace;
    font-weight: 400;
    font-size: 150px;
    letter-spacing: -14px;
    line-height: 1;
    color: var(--brown);
  }
  .tagline {
    position: absolute;
    top: 308px;
    left: 0;
    width: 100%;
    margin: 0;
    text-align: center;
    font-family: "Share Tech Mono", monospace;
    font-size: 70px;
    letter-spacing: -5.5px;
    line-height: 1;
    color: var(--burnt-orange);
  }
  .tagline-dot {
    display: inline-block;
    width: 22px;
    height: 22px;
    margin: 0 20px 0 14px;
    border-radius: 50%;
    background: var(--burnt-orange);
    vertical-align: 12px;
  }
  .brand-mark {
    position: absolute;
    top: 418px;
    left: 478px;
    width: 232px;
    height: 250px;
  }
  .origin {
    position: absolute;
    top: 730px;
    left: 0;
    width: 100%;
    margin: 0;
    text-align: center;
    font-family: "Space Mono", monospace;
    font-weight: 700;
    font-size: 31px;
    line-height: 34px;
    letter-spacing: 8px;
    color: var(--ink);
  }
  .roast-panel {
    position: absolute;
    top: 1006px;
    left: 124px;
    width: 948px;
    height: 186px;
    background: var(--lime-deep);
    font-family: "Lato", sans-serif;
    font-size: 24px;
    color: var(--panel-ink);
  }
  .roast-panel p {
    position: absolute;
    left: 54px;
    margin: 0;
    line-height: 1;
  }
  .roast-name { top: 17px; }
  .roast-notes { top: 79px; }
  .roast-size { top: 140px; }
</style>
</head>
<body>
  <main class="label">
    <h1 class="brand-name">Fenn-Brew</h1>
    <p class="tagline">Organic Coffee<span class="tagline-dot" aria-hidden="true"></span>Smoothies</p>

    <svg class="brand-mark" viewBox="0 0 232 250" aria-hidden="true">
      <circle cx="116" cy="125" r="110" fill="var(--bean-brown)"/>
    </svg>

    <p class="origin">100% Premium Arabica Nicaraguan<br>Coffee"<br>Organic, Rain Forest &amp; Mountain<br>Shade Grown</p>

    <section class="roast-panel">
      <p class="roast-name">Medium Roast</p>
      <p class="roast-notes">Full body, bold flavor, nutty, hints of chocolate, with a distinct &amp; flavorful aroma.</p>
      <p class="roast-size">12 oz</p>
    </section>
  </main>
</body>
</html>
```